Online interactive calendar for training organisation

We have a new website being made and need a design for an online calendar that is interactive and very simple and easy to use. On our main page this calendar will include all of our courses (approx 30 different ones with up to 8 different locations). On our sub pages which have course information, the calendar will only include details of that specific course. Details needed are: Course code, course name/title, date, duration (1/2 day - 5 days), location, price, discount price. Maybe also a key for available or limited spots left? We want a section at the top of the calendar to be able to filter by location or course, and maybe to filter by month also? I have included a spreadsheet with a sample of our courses with this information. Also a sample draft of the main page on our new webpage to show the colour green which is our company colour. Main notes - we want as simple, effective and easy to use as possible.
We will need to know what plug in we can use to get the design you have created.

Target Market(s)

Mining and construction - both companies and individuals

Number of Pages Required

1 page

Colors
cadf82

Requirements
Must have
• Be simple, easy to use, effective.

```html
<!DOCTYPE html>
<html lang="en">
<head>
<meta charset="utf-8">
<title>Ridgeline Safety – Time Table</title>
<link rel="stylesheet" href="https://fonts.googleapis.com/css2?family=Open+Sans:wght@400;600;800&family=PT+Sans&display=swap">
<style>
:root{
  --green:#7cb02c;
  --green-bar:#8bc42f;
  --green-dark:#3d7f27;
  --grey-band:#e6e6e6;
  --grey-top:#e9e9e9;
  --row-a:#e4e4e4;
  --row-b:#f1f1f1;
  --ink:#2b2b2b;
  --ink-soft:#444;
  --footer:#1d1d1d;
  --footer-ink:#a9a9a9;
  --white:#fff;
  --red:#d9242b;
}
*{box-sizing:border-box;margin:0;padding:0}
html,body{width:703px;height:1200px;overflow:hidden}
body{position:relative;font-family:"Open Sans",sans-serif;color:var(--ink);background:var(--white)}
.abs{position:absolute}

/* top bar */
.topbar{left:0;top:0;width:703px;height:23px;background:var(--grey-top)}
.social{display:flex;gap:8px;align-items:center}
.social span{display:block;width:7px;height:7px;border-radius:50%;background:#555}
.topbar .social{position:absolute;left:84px;top:8px}
.student-btn{position:absolute;left:403px;top:2px;width:70px;height:19px;background:var(--green-bar);color:var(--ink);font-size:6.6px;display:flex;align-items:center;justify-content:center;gap:4px}
.search{position:absolute;left:478px;top:2px;width:140px;height:19px;background:var(--white);border:1px solid #ccc;font-size:6.6px;color:#999;display:flex;align-items:center;justify-content:space-between;padding:0 6px 0 9px}

/* header */
.header{left:0;top:23px;width:703px;height:51px;background:var(--white)}
.brand{position:absolute;left:84px;top:12px;display:flex;align-items:center;gap:6px}
.brand-dot{width:28px;height:28px;border-radius:50%;background:var(--red)}
.brand-name{font-size:12px;font-weight:800;color:var(--red);line-height:1}
.brand-tag{position:absolute;left:142px;top:34px;font-size:5.6px;color:var(--ink-soft)}
.nav{position:absolute;right:85px;top:21px;display:flex;gap:18px;font-size:7.2px;color:var(--ink-soft)}
.nav .active{color:var(--green-dark)}

/* difference section */
.difference{left:0;top:74px;width:703px;height:361px;background:var(--grey-band)}
.section-title{position:absolute;left:0;width:703px;text-align:center;font-family:"PT Sans",sans-serif;color:var(--green);font-weight:400;letter-spacing:.2px}
.section-sub{position:absolute;left:0;width:703px;text-align:center;font-size:8.6px;color:var(--ink)}
.tile{position:absolute;width:98px}
.tile-img{width:98px;height:85px}
.tile-label{font-size:7px;text-align:center;margin-top:4px;color:var(--ink)}

/* filters */
.filter{position:absolute;top:539px;width:175px;height:28px;border:1px solid #bdbdbd;background:var(--white);display:flex;align-items:center;justify-content:space-between;padding:0 9px;font-size:8.4px;font-weight:600}
.filter em{font-style:normal;font-weight:400;color:var(--green-dark)}

/* table */
.timetable{left:84px;top:586px;width:535px;border-collapse:collapse;font-size:6.5px;color:var(--ink-soft)}
.timetable th{background:var(--green-bar);color:var(--white);font-weight:400;font-size:7.8px;text-align:left;height:24px;padding:0 5px;border-right:1px solid rgba(255,255,255,.55);white-space:nowrap}
.timetable th:first-child,.timetable td:first-child{padding-left:9px}
.timetable td{height:34px;vertical-align:top;padding:7px 5px 0;border-right:1px solid #fff;line-height:1.3}
.timetable tbody tr:nth-child(odd){background:var(--row-a)}
.timetable tbody tr:nth-child(even){background:var(--row-b)}
.star{color:var(--red)}
.key{left:0;top:787px;width:703px;text-align:center;font-size:6.6px;color:var(--ink-soft)}

/* banner */
.banner{left:0;top:843px;width:703px;height:234px;background:linear-gradient(90deg,#8b7f6c 0%,#a08a6c 45%,#b9852f 70%,#7a5a22 100%)}
.banner-title{position:absolute;left:84px;top:92px;font-size:25px;line-height:29px;font-weight:800;color:var(--white)}
.btn-more{position:absolute;left:85px;top:149px;width:51px;height:18px;background:var(--green-bar);color:var(--white);font-size:6.4px;display:flex;align-items:center;justify-content:center}

/* contact */
.contact{left:0;top:1101px;width:703px;display:flex;justify-content:center;gap:38px;font-size:10px;color:var(--ink-soft)}
.contact span{display:flex;align-items:center;gap:5px}

/* footer */
.footer{left:0;top:1144px;width:703px;height:56px;background:var(--footer);color:var(--footer-ink);font-size:6.8px}
.footer-links{position:absolute;left:84px;top:13px;display:flex;gap:7px}
.copyright{position:absolute;left:84px;top:31px}
.footer .social{position:absolute;right:85px;top:25px}
.footer .social span{background:#777}
</style>
</head>
<body>

<div class="abs topbar">
  <div class="social"><span></span><span></span><span></span><span></span></div>
  <div class="student-btn">
    <svg width="7" height="7" viewBox="0 0 10 10"><path d="M1 4h4V2l3 3-3 3V6H1z" fill="#222"/><path d="M6 1h3v8H6" fill="none" stroke="#222" stroke-width="1.2"/></svg>
    Student Access
  </div>
  <div class="search">Search
    <svg width="8" height="8" viewBox="0 0 10 10"><circle cx="4" cy="4" r="3" fill="none" stroke="#222" stroke-width="1.5"/><path d="M6.3 6.3L9 9" stroke="#222" stroke-width="1.6"/></svg>
  </div>
</div>

<header class="abs header">
  <div class="brand"><div class="brand-dot"></div><div class="brand-name">RIDGELINE SAFETY</div></div>
  <div class="brand-tag">SAFETY AND TRAINING</div>
  <nav class="nav">
    <span class="active">Home</span><span>Courses</span><span>Our Services</span><span>About Us</span><span>Funding</span><span>Locations</span><span>Contact Us</span>
  </nav>
</header>

<section class="abs difference">
  <h1 class="section-title" style="top:40px;font-size:29px">THE RIDGELINE SAFETY DIFFERENCE</h1>
  <p class="section-sub" style="top:74px">Commited to helping our students succeed.</p>

  <div class="tile" style="left:84px;top:99px"><div class="tile-img" role="img" aria-label="Excavator loading a mining truck" style="background:linear-gradient(180deg,#9fb3c8,#8a7a5c)"></div><p class="tile-label">All Courses</p></div>
  <div class="tile" style="left:193px;top:99px"><div class="tile-img" role="img" aria-label="Workers in hard hats at an industrial plant" style="background:linear-gradient(180deg,#7d7f80,#5a4c40)"></div><p class="tile-label">Funded Courses</p></div>
  <div class="tile" style="left:302px;top:99px"><div class="tile-img" role="img" aria-label="Haul truck in a mine" style="background:linear-gradient(180deg,#c9b7a3,#6e5240)"></div><p class="tile-label">Mining</p></div>
  <div class="tile" style="left:411px;top:99px"><div class="tile-img" role="img" aria-label="Excavator against a stormy sky" style="background:linear-gradient(180deg,#5d6670,#3c3f44)"></div><p class="tile-label">Standard 11</p></div>
  <div class="tile" style="left:520px;top:99px"><div class="tile-img" role="img" aria-label="Worker abseiling on a building facade" style="background:linear-gradient(90deg,#2e3a4d,#6b7f99)"></div><p class="tile-label">Work Safety at Heights</p></div>

  <div class="tile" style="left:84px;top:212px"><div class="tile-img" role="img" aria-label="Business handshake across a table" style="background:linear-gradient(180deg,#b8b4ae,#6b5a4d)"></div><p class="tile-label">Corporate Clients</p></div>
  <div class="tile" style="left:193px;top:212px"><div class="tile-img" role="img" aria-label="Person studying at a laptop" style="background:linear-gradient(180deg,#d8d3cc,#8c8a86)"></div><p class="tile-label">Online Courses</p></div>
  <div class="tile" style="left:302px;top:212px"><div class="tile-img" role="img" aria-label="Engineers reviewing plans on site" style="background:linear-gradient(180deg,#8a7c66,#3e4a5e)"></div><p class="tile-label">RPL’s &amp; VOC’s</p></div>
  <div class="tile" style="left:411px;top:212px"><div class="tile-img" role="img" aria-label="Workers on scaffolding at sunset" style="background:linear-gradient(180deg,#7a8da0,#e0903a 70%,#2a1e14)"></div><p class="tile-label">Plant &amp; Equipment</p></div>
  <div class="tile" style="left:520px;top:212px"><div class="tile-img" role="img" aria-label="Construction worker on a building site" style="background:linear-gradient(180deg,#a9c2d8,#8b8478)"></div><p class="tile-label">Construction</p></div>
</section>

<h2 class="section-title" style="top:479px;font-size:29px">TIME TABLE</h2>
<p class="section-sub" style="top:513px">Cras sollicitudin cursus dui eu placerat</p>

<div class="filter" style="left:84px"><span>Location : <em>Mackay</em></span>
  <svg width="8" height="10" viewBox="0 0 8 10"><path d="M4 0a3.5 3.5 0 0 0-3.5 3.5C.5 6 4 10 4 10s3.5-4 3.5-6.5A3.5 3.5 0 0 0 4 0z" fill="#222"/><circle cx="4" cy="3.5" r="1.3" fill="#fff"/></svg></div>
<div class="filter" style="left:264px"><span>Month</span>
  <svg width="11" height="11" viewBox="0 0 11 11"><rect x=".7" y="1.7" width="9.6" height="8.6" fill="none" stroke="#222" stroke-width="1"/><rect x=".7" y="1.7" width="9.6" height="2" fill="#222"/><path d="M3 0v3M8 0v3M1 6h9M1 8h9M3.5 4v6M5.5 4v6M7.5 4v6" stroke="#222" stroke-width=".6"/></svg></div>
<div class="filter" style="left:444px"><span>Course</span>
  <svg width="11" height="9" viewBox="0 0 11 9"><g fill="#222"><rect x="0" y="0" width="2" height="2"/><rect x="0" y="3.5" width="2" height="2"/><rect x="0" y="7" width="2" height="2"/><rect x="3" y=".3" width="8" height="1.4"/><rect x="3" y="3.8" width="8" height="1.4"/><rect x="3" y="7.3" width="8" height="1.4"/></g></svg></div>

<table class="abs timetable">
  <colgroup><col style="width:112px"><col style="width:89px"><col style="width:47px"><col style="width:61px"><col style="width:89px"><col style="width:56px"><col style="width:81px"></colgroup>
  <thead><tr><th>Course code &amp; title</th><th>Course time</th><th>Time</th><th>Duration</th><th>Location</th><th>Price</th><th>Member discount</th></tr></thead>
  <tbody>
    <tr><td>RIIMPO308E Forklift <span class="star">*</span></td><td>Wednesday,<br>October 30, 2019</td><td>8 am</td><td>3 days</td><td>Mackay</td><td>$ 500.00</td><td>$ 100.00</td></tr>
    <tr><td>HLTAID001 First Aid -<br>practical only</td><td>Saturday,<br>November 30, 2019</td><td>8 am</td><td>1/2 day</td><td>Mackay</td><td>$ 80.00</td><td></td></tr>
    <tr><td>Defensive Driving <span class="star">*</span></td><td>Wednesday,<br>November 27, 2019</td><td>8 am</td><td>1 day</td><td>Mackay</td><td>$ 275.00</td><td></td></tr>
    <tr><td>HLTAID001 First Aid -<br>practical only</td><td>Wednesday,<br>January 15, 2020</td><td>1 pm</td><td>1/2 day</td><td>Mackay</td><td>$ 80.00</td><td></td></tr>
    <tr><td>RIIMPO308E Forklift</td><td>Wednesday,<br>October 30, 2019</td><td>8 am</td><td>3 days</td><td>Mackay</td><td>$ 80.00</td><td></td></tr>
  </tbody>
</table>
<p class="abs key"><span class="star">*</span> Limited spots left</p>

<section class="abs banner" role="img" aria-label="Large mining haul trucks on a dusty quarry road">
  <h2 class="banner-title">Pellentesque convallis<br>molestie enim</h2>
  <div class="btn-more">READ MORE</div>
</section>

<div class="abs contact">
  <span><svg width="7" height="9" viewBox="0 0 8 10"><path d="M4 0a3.5 3.5 0 0 0-3.5 3.5C.5 6 4 10 4 10s3.5-4 3.5-6.5A3.5 3.5 0 0 0 4 0z" fill="#333"/><circle cx="4" cy="3.5" r="1.3" fill="#fff"/></svg>18 Quarry Lane, Ridgeview QLD 4000</span>
  <span><svg width="10" height="8" viewBox="0 0 10 8"><rect width="10" height="8" fill="#333"/><path d="M0 .5l5 4 5-4" fill="none" stroke="#fff" stroke-width=".8"/></svg>hello@ridgelinesafety.example</span>
</div>

<footer class="abs footer">
  <div class="footer-links"><span>Home</span><span>|</span><span>Courses</span><span>|</span><span>Our Services</span><span>|</span><span>About Us</span><span>|</span><span>Funding</span><span>|</span><span>Locations</span><span>|</span><span>Contact Us</span></div>
  <p class="copyright">Copyright © 2019 Ridgeline Safety. All rights reserved.</p>
  <div class="social"><span></span><span></span><span></span><span></span></div>
</footer>

</body>
</html>
```